The Perfect Business Card for PineHarbor

I am looking for a business card which beautifully incorporates my logo, reflects my business and looks special, elegant and clean.

```html
<!DOCTYPE html>
<html lang="en">
<head>
<meta charset="utf-8">
<title>PineHarbor Business Card</title>
<link rel="stylesheet" href="https://fonts.googleapis.com/css2?family=Cinzel:wght@400&family=Cormorant+Garamond:wght@700&family=Roboto:wght@400;500&display=swap">
<style>
  :root {
    --page-bg: #dcdcdc;
    --card-white: #ffffff;
    --brand-green: #7c9d48;
    --brand-green-deep: #5e7238;
    --logo-green: #6f8f3c;
    --ink: #1c1c1c;
    --ink-soft: #2a2a2a;
  }
  * { box-sizing: border-box; margin: 0; padding: 0; }
  html, body { width: 1200px; height: 900px; overflow: hidden; }
  body { background: var(--page-bg); position: relative; font-family: "Roboto", Arial, sans-serif; }

  .card { position: absolute; left: 255px; width: 690px; height: 394px; overflow: hidden; }
  .card--front { top: 45px; background: var(--brand-green); }
  .card--back { top: 464px; background: var(--card-white); }

  .brand { position: absolute; display: flex; align-items: center; }
  .brand__mark { border-radius: 50%; border-style: solid; flex: none; }
  .brand__name { font-family: "Cinzel", "Times New Roman", serif; font-weight: 400; line-height: 1; white-space: nowrap; }

  .card--front .brand { left: 0; right: 0; top: 150px; justify-content: center; gap: 22px; }
  .card--front .brand__mark { width: 84px; height: 84px; border-width: 2px; border-color: var(--card-white); }
  .card--front .brand__name { font-size: 60px; color: var(--card-white); }

  .card--back .brand { left: 0; right: 0; top: 40px; justify-content: center; gap: 14px; }
  .card--back .brand__mark { width: 50px; height: 50px; border-width: 1.5px; border-color: var(--logo-green); }
  .card--back .brand__name { font-size: 36px; color: var(--logo-green); }

  .person { position: absolute; left: 0; right: 0; top: 160px; text-align: center; }
  .person__name { font-family: "Cormorant Garamond", Georgia, serif; font-weight: 700; font-size: 40px; letter-spacing: 0.02em; color: var(--ink); line-height: 1; text-transform: uppercase; }
  .person__role { margin-top: 6px; font-family: "Roboto", Arial, sans-serif; font-weight: 500; font-size: 24px; letter-spacing: 0.52em; padding-left: 0.52em; color: var(--ink-soft); line-height: 1; text-transform: uppercase; }

  .contact { position: absolute; left: 0; right: 0; display: flex; justify-content: center; gap: 38px; font-size: 21px; color: var(--ink-soft); }
  .contact--phone { top: 272px; }
  .contact--web { top: 316px; }
  .contact__item { display: flex; align-items: center; gap: 10px; }
  .contact__icon { width: 20px; height: 20px; fill: var(--brand-green-deep); flex: none; }

  .band { position: absolute; bottom: 0; height: 19px; }
  .band--light { left: 0; width: 313px; background: var(--brand-green); }
  .band--dark { left: 321px; right: 0; background: var(--brand-green-deep); }
</style>
</head>
<body>

<section class="card card--front" aria-label="Card front">
  <div class="brand">
    <span class="brand__mark"></span>
    <span class="brand__name">PineHarbor</span>
  </div>
</section>

<section class="card card--back" aria-label="Card back">
  <div class="brand">
    <span class="brand__mark"></span>
    <span class="brand__name">PineHarbor</span>
  </div>

  <div class="person">
    <p class="person__name">Marek Kowalin</p>
    <p class="person__role">Consultant</p>
  </div>

  <div class="contact contact--phone">
    <span class="contact__item">
      <svg class="contact__icon" viewBox="0 0 24 24" aria-hidden="true"><path d="M6.6 10.8a15.1 15.1 0 0 0 6.6 6.6l2.2-2.2c.3-.3.7-.4 1-.2 1.1.4 2.3.6 3.6.6.6 0 1 .4 1 1V20c0 .6-.4 1-1 1A17 17 0 0 1 3 4c0-.6.4-1 1-1h3.5c.6 0 1 .4 1 1 0 1.3.2 2.5.6 3.6.1.3 0 .7-.2 1z"/></svg>
      044-555 018 273
    </span>
  </div>

  <div class="contact contact--web">
    <span class="contact__item">
      <svg class="contact__icon" viewBox="0 0 24 24" aria-hidden="true"><path d="M2 5h20v14H2zM4 7v.4l8 5.2 8-5.2V7zm0 2.8V17h16V9.8l-8 5.2z"/></svg>
      info@pineharbor.com
    </span>
    <span class="contact__item">
      <svg class="contact__icon" viewBox="0 0 24 24" aria-hidden="true" fill="none" stroke="#5e7238" stroke-width="1.6" style="fill:none"><circle cx="12" cy="12" r="9.5"/><ellipse cx="12" cy="12" rx="4.2" ry="9.5"/><path d="M2.5 12h19M4 7h16M4 17h16"/></svg>
      www.pineharbor.com
    </span>
  </div>

  <div class="band band--light"></div>
  <div class="band band--dark"></div>
</section>

</body>
</html>
```